US Recruiting Firm Needs Dynamic Tri-Fold Brochure

Need tri-fold professional brochure for HR recruiting and consulting firm based in the US.

Target Market(s)

Clients seeking administrative and human resources talent

Industry/Entity Type

Recruitment

Font styles to use
Sans Serif

Requirements
Should not have
• No weird shapes
• No heavy geometric shapes -- I prefer curvy lines
• Not a dark brochure

```html
<!DOCTYPE html>
<html lang="en">
<head>
<meta charset="utf-8">
<title>Piedmont Talent Partners – Tri-Fold Brochure</title>
<link rel="stylesheet" href="https://fonts.googleapis.com/css2?family=Lato:wght@300;400;700&family=Open+Sans:wght@300;400;600;700&family=Libre+Baskerville:wght@700&display=swap">
<style>
  :root {
    --purple: #a3237f;
    --navy: #0f3b5c;
    --orange: #f06a12;
    --green: #8dc21f;
    --ink: #2b2b2b;
    --paper: #ffffff;
    --backdrop: #e4e4e4;
  }
  * { margin: 0; padding: 0; box-sizing: border-box; }
  html, body { width: 1200px; height: 1200px; overflow: hidden; background: var(--backdrop); }
  .brochure {
    position: absolute; left: 50px; top: 209px;
    width: 873px; height: 620px;
    transform: scale(1.26); transform-origin: 0 0;
    background: var(--paper);
    box-shadow: 0 2px 8px rgba(0,0,0,.18);
    font-family: "Lato", sans-serif; color: var(--ink);
    overflow: hidden;
  }
  .shapes, .photo-left { position: absolute; left: 0; top: 0; }
  .fold-shade { position: absolute; top: 0; height: 620px; }
  .fold-shade.middle { left: 560px; width: 27px; background: linear-gradient(90deg, rgba(0,0,0,0), rgba(0,0,0,.05)); }
  .fold-shade.right { left: 585px; width: 30px; background: linear-gradient(90deg, rgba(0,0,0,.05), rgba(0,0,0,0)); }

  .section-title { position: absolute; left: 20px; color: #fff; font-weight: 400; }
  .trusted-title { top: 188px; font-size: 17px; }
  .choose-title { top: 314px; left: 26px; font-size: 13.5px; }
  .mission-title { top: 467px; left: 26px; font-size: 13.5px; }

  .copy { position: absolute; left: 25px; width: 260px; font-size: 9.3px; line-height: 12px; }
  .copy.about { top: 234px; }
  .copy.mission { top: 508px; }
  .benefits { position: absolute; left: 38px; top: 351px; list-style: none; font-size: 9.3px; line-height: 14.2px; }
  .benefits li { position: relative; }
  .benefits li::before { content: ""; position: absolute; left: -10px; top: 5px; width: 4px; height: 4px; border-radius: 50%; background: var(--orange); }

  .brand { position: absolute; display: flex; align-items: center; color: var(--navy); }
  .brand-dot { border-radius: 50%; background: var(--purple); flex: none; }
  .brand-name { font-weight: 700; text-align: center; line-height: 1; letter-spacing: .02em; }
  .brand-tag { display: block; font-weight: 700; letter-spacing: 0; margin-top: 2px; }
  .brand.small { left: 327px; top: 184px; }
  .brand.small .brand-dot { width: 26px; height: 26px; margin-right: 6px; }
  .brand.small .brand-name { font-size: 12.5px; }
  .brand.small .brand-tag { font-size: 6.5px; }
  .brand.large { left: 614px; top: 52px; }
  .brand.large .brand-dot { width: 38px; height: 38px; margin-right: 8px; }
  .brand.large .brand-name { font-size: 17px; }
  .brand.large .brand-tag { font-size: 8.5px; }

  .contact-intro { position: absolute; left: 330px; top: 242px; font-size: 9.3px; line-height: 12px; }
  .contact-intro strong { display: block; color: var(--navy); font-size: 15px; line-height: 17px; font-weight: 700; }
  .contact-list { position: absolute; left: 331px; top: 304px; list-style: none; font-size: 9.3px; }
  .contact-list li { display: flex; align-items: center; height: 29px; }
  .contact-icon { width: 19px; height: 19px; border-radius: 50%; background: var(--purple); display: flex; align-items: center; justify-content: center; margin-right: 12px; }

  .photo-right {
    position: absolute; left: 585px; top: 148px; width: 288px; height: 229px;
    background: linear-gradient(160deg, #f1f3f5 0%, #c9ced4 35%, #5b6068 70%, #3a3d44 100%);
  }
  .headline {
    position: absolute; left: 585px; width: 288px; top: 405px;
    display: flex; flex-direction: column; align-items: center;
    color: #fff; font-family: "Open Sans", sans-serif; font-weight: 400;
  }
  .headline .lead { font-size: 27px; font-weight: 600; line-height: 30px; padding-left: 10px; white-space: nowrap; }
  .headline .sub { font-size: 23px; font-weight: 300; line-height: 25px; }
  .headline .tag { background: #fff; color: var(--purple); font-family: "Libre Baskerville", serif; font-weight: 700; font-size: 12.5px; line-height: 18px; padding: 0 4px; }
  .headline .tag.first { margin-top: 4px; }
  .headline .plain { font-size: 13.5px; font-weight: 400; line-height: 20px; margin: 2px 0 2px; }
  .website { position: absolute; left: 640px; top: 564px; width: 233px; text-align: center; color: #fff; font-family: "Open Sans", sans-serif; font-size: 11px; letter-spacing: .18em; }
</style>
</head>
<body>
<div class="brochure">

  <svg class="photo-left" width="873" height="620" role="img" aria-label="Photo of a smiling businesswoman with colleagues in a meeting room">
    <defs>
      <linearGradient id="meeting" x1="0" y1="0" x2="1" y2="1">
        <stop offset="0" stop-color="#e9e6e2"/>
        <stop offset=".45" stop-color="#b9b4ad"/>
        <stop offset="1" stop-color="#6d6f76"/>
      </linearGradient>
    </defs>
    <polygon points="0,0 288,0 256,160 0,160" fill="url(#meeting)"/>
  </svg>

  <svg class="shapes" width="873" height="620" aria-hidden="true">
    <polygon points="230,0 381,0 338,90 200,90" fill="var(--orange)" opacity=".92"/>
    <polygon points="296,90 354,90 308,160 252,160" fill="var(--green)"/>
    <polygon points="0,184 255,184 244,219 0,219" fill="var(--purple)"/>
    <polygon points="259,184 267,184 256,219 248,219" fill="var(--navy)"/>
    <polygon points="0,309 158,309 149,337 0,337" fill="var(--purple)"/>
    <polygon points="162,309 171,309 162,337 153,337" fill="var(--navy)"/>
    <polygon points="0,462 115,462 106,490 0,490" fill="var(--purple)"/>
    <polygon points="119,462 128,462 119,490 110,490" fill="var(--navy)"/>
    <polygon points="558,377 873,377 873,557 633,557 621,587 448,587" fill="var(--purple)"/>
    <polygon points="633,557 873,557 873,587 621,587" fill="var(--navy)"/>
    <polygon points="88,587 448,587 436,620 66,620" fill="var(--navy)"/>
  </svg>

  <div class="fold-shade middle"></div>
  <div class="fold-shade right"></div>

  <!-- Inside panel -->
  <h2 class="section-title trusted-title">A Trusted Recruiting Partner</h2>
  <p class="copy about">We have over 20 years of recruiting and human resources experience.<br>Our recruiters have the expertise, insights, and passion to bring value-added recruiting services to your company.<br>We have a track record of excellence.</p>

  <h2 class="section-title choose-title">Why Choose Us?</h2>
  <ul class="benefits">
    <li>We are HR experts dedicated to recruiting</li>
    <li>HR professionals</li>
    <li>Highly Qualified talent network</li>
    <li>Comprehensive pre-screening</li>
    <li>Simplified recruiting process</li>
    <li>Reasonable placement fees</li>
    <li>90-Day replacement guarantee</li>
  </ul>

  <h2 class="section-title mission-title">Our Mission</h2>
  <p class="copy mission">We have a two-fold mission. We help companies hire the best HR staff to help meet organizational goals and cultivate a highly engaged, productive workforce. We also help HR talent find fulfilling work and careers with awesome companies.</p>

  <!-- Contact panel -->
  <div class="brand small">
    <span class="brand-dot"></span>
    <span class="brand-name">PIEDMONT TALENT<br>PARTNERS<span class="brand-tag">Human Resources Staffing &amp; Consulting</span></span>
  </div>
  <p class="contact-intro">To learn more and request a<strong>FREE</strong>consultation, contact us today.</p>
  <ul class="contact-list">
    <li><span class="contact-icon"><svg width="10" height="10" viewBox="0 0 10 10"><path d="M2 1 L3.6 1 L4.2 3 L3.2 3.8 Q4 5.8 6.2 6.8 L7 5.8 L9 6.4 L9 8 Q8.6 9 7.6 9 Q1 8 1 2 Q1.2 1 2 1Z" fill="#fff"/></svg></span>Phone to be determined</li>
    <li><span class="contact-icon"><svg width="10" height="10" viewBox="0 0 10 10" fill="none" stroke="#fff" stroke-width="1"><circle cx="5" cy="5" r="4"/><ellipse cx="5" cy="5" rx="1.8" ry="4"/><line x1="1" y1="5" x2="9" y2="5"/></svg></span>Website – to be determined</li>
    <li><span class="contact-icon"><svg width="10" height="10" viewBox="0 0 10 10" fill="none" stroke="#fff" stroke-width="1"><rect x="1" y="2.5" width="8" height="5.5"/><polyline points="1,2.5 5,5.8 9,2.5"/></svg></span>Email to be determined</li>
  </ul>

  <!-- Cover panel -->
  <div class="brand large">
    <span class="brand-dot"></span>
    <span class="brand-name">PIEDMONT TALENT<br>PARTNERS<span class="brand-tag">Human Resources Staffing &amp; Consulting</span></span>
  </div>
  <div class="photo-right" role="img" aria-label="Photo of business professionals shaking hands across a meeting table"></div>
  <h1 class="headline">
    <span class="lead">SPECIALIZING IN</span>
    <span class="sub">Administrative</span>
    <span class="tag first">PROFESSIONAL</span>
    <span class="plain">And executive</span>
    <span class="tag">HR TALENT</span>
  </h1>
  <p class="website">your website goes here</p>
</div>
</body>
</html>
```